Business Card Design

I want to pull elements/colors from Website. Attached is a screen shot. Do not want any buildings/building graphics/construction clichés. This is for a construction management firm but I want to keep it broad enough that I can expand into other areas. I do not want the logo to be limited. Thank you.
Updates

Please review the screen shot of the website. Please use the font and color of Brackwell Holdings, LLC on the website. Please use the tag line "Construction Management in the Palm Beaches" Please show contractor license ... CGC 7390462 You may use the back for the contact information. Please no phone/house icons. It does not have to be a black card. Thank you.

Target Market(s)

Professional people with money. Owners, Architects, Engineers, Developers, Real Estate Agents etc.

Industry/Entity Type

Construction

Contact Information for Business Card

Brackwell Holdings, LLC
Construction Management

Dean T Brackwell
418 Ostrander Court #73
North Palm Beach, FL 33412
(561) 555-0187
www.BrackwellHoldings.example

Requirements
Must have
• Clean, crisp, modern.

Broad enough that it is not trapped into a particular industry.

My goal is to expand into different markets, different industries.

Should not have
• The back of the card should not be colored in any way. Rubs off on other cards.

Do not want any buildings/building graphics/construction clichés.

```html
<!DOCTYPE html>
<html lang="en">
<head>
<meta charset="utf-8">
<title>Brackwell Holdings — Business Card</title>
<link rel="stylesheet" href="https://fonts.googleapis.com/css2?family=Open+Sans:wght@400;700&display=swap">
<style>
  :root {
    --page-bg: #e4e2e1;
    --card-base: #2b2627;
    --facet-light: #3b3334;
    --facet-mid: #332c2d;
    --facet-dark: #262122;
    --ink: #ffffff;
    --ink-soft: #f1eeee;
  }
  html, body {
    margin: 0;
    width: 1200px;
    height: 1000px;
    overflow: hidden;
    background: var(--page-bg);
    font-family: "Open Sans", sans-serif;
  }
  .card {
    position: absolute;
    left: 100px;
    top: 214px;
    width: 1000px;
    height: 572px;
    background: var(--card-base);
    overflow: hidden;
    color: var(--ink);
  }
  .card-facets {
    position: absolute;
    inset: 0;
    width: 100%;
    height: 100%;
  }
  .brand {
    position: absolute;
    left: 90px;
    top: 262px;
    width: 560px;
    line-height: 1.15;
  }
  .brand-name {
    margin: 0;
    font-size: 46px;
    font-weight: 700;
    letter-spacing: 0.5px;
  }
  .brand-descriptor {
    margin: 2px 0 0;
    font-size: 30px;
    font-weight: 400;
    color: var(--ink-soft);
  }
  .brand-tagline {
    margin: 10px 0 0;
    font-size: 21px;
    font-weight: 400;
    color: var(--ink-soft);
  }
  .contact {
    position: absolute;
    left: 640px;
    top: 92px;
    font-size: 24px;
    line-height: 1.25;
  }
  .contact-name {
    margin: 0 0 26px;
    font-size: 30px;
    font-weight: 400;
  }
  .contact-line {
    margin: 0 0 22px 34px;
  }
  .contact-license {
    margin: 0 0 0 34px;
    font-size: 21px;
    color: var(--ink-soft);
  }
  .website {
    position: absolute;
    right: 60px;
    bottom: 52px;
    margin: 0;
    font-size: 28px;
    letter-spacing: 0.3px;
  }
</style>
</head>
<body>
  <section class="card" aria-label="Brackwell Holdings business card">
    <svg class="card-facets" viewBox="0 0 1000 572" preserveAspectRatio="none" aria-hidden="true">
      <polygon points="0,0 610,0 0,500" fill="var(--facet-light)"/>
      <polygon points="610,0 1000,0 1000,330" fill="var(--facet-light)"/>
      <polygon points="610,0 1000,330 700,330" fill="var(--facet-mid)"/>
      <polygon points="530,70 610,0 700,330 640,330" fill="var(--facet-dark)"/>
    </svg>

    <div class="brand">
      <h1 class="brand-name">Brackwell Holdings</h1>
      <p class="brand-descriptor">LLC Construction Management</p>
      <p class="brand-tagline">Construction Management in the Palm Beaches</p>
    </div>

    <div class="contact">
      <p class="contact-name">Dean T Brackwell</p>
      <p class="contact-line">(561) 555-0187</p>
      <p class="contact-line">418 Ostrander Court #73<br>North Palm Beach, FL 33412</p>
      <p class="contact-license">License CGC 7390462</p>
    </div>

    <p class="website">www.BrackwellHoldings.example</p>
  </section>
</body>
</html>
```